PPT :The Art Market in a changing world

Nr of Slides :19

To do
As I have no PDF Converter from PDF to PPT

1 All slides needs to be put in the LANDSCAPE format(horizontal)
2 I need to be able to change every picture /title (so no PDF)
3 Style & Color =Basic is red and white see slide 1
4 Every Title must be in a Red Block & White Letters
5 I need to be able to change every picture text in order to be able to update

-Slide 5 from the PDF : date 2016 needs to be 2018
-Slide 8. from the PDF :date 17 should be 2018
-Slide 9. from the PDF :date 2015 should be 2018

-Update by adding the latest related info

Target Market(s)

Art Professionals
Showing the power off the Mobile Phone /Computer /Platforms as a tool for the new art economy
Therefore I added some pictures of mobile phones ..

Font styles to use
Sans Serif

Colors
ec1f27
0255a3
ffffff

Requirements
Must have
• Attached files have the shade/tone of red I'd like you to use in the design.
• I need to be able to update every part of the slide (Title,date, picture,graph)
• Mention on the last slide my social media /logo plus account
• Flikora. Lucien Dramonte
• Workvine: Lucien Dramonte
• Chirply: DramonteLucien
Nice to have
• Possibility to insert a video (Flikora)

```html
<!DOCTYPE html>
<html lang="en">
<head>
<meta charset="utf-8">
<title>The New Art Economy – Slide Deck</title>
<link rel="stylesheet" href="https://fonts.googleapis.com/css2?family=Teko:wght@400;500&family=Josefin+Sans:wght@300;400&family=Questrial&family=Open+Sans:wght@400;700&display=swap">
<style>
  :root {
    --brand-red: #ec1f27;
    --ink: #2b2b2b;
    --charcoal: #3a3a3a;
    --paper: #ffffff;
    --stage-light: #f1f1f1;
    --stage-grey: #c8c8c8;
    --muted: #555555;
  }
  html, body {
    margin: 0;
    padding: 0;
    width: 912px;
    height: 1200px;
    overflow: hidden;
    background: var(--stage-light);
  }
  .deck-board { display: block; width: 912px; height: 1200px; }
  .title-condensed { font-family: "Teko", "Oswald", sans-serif; font-weight: 500; }
  .title-wide { font-family: "Josefin Sans", sans-serif; font-weight: 300; }
  .quote-text { font-family: "Questrial", sans-serif; }
  .body-text { font-family: "Open Sans", sans-serif; }
  .red-fill { fill: var(--brand-red); }
  .ink-fill { fill: var(--ink); }
  .white-fill { fill: var(--paper); }
  .charcoal-fill { fill: var(--charcoal); }
  .muted-fill { fill: var(--muted); }
  .slide-shadow { filter: drop-shadow(0 6px 6px rgba(0,0,0,0.18)); }
</style>
</head>
<body>
<svg class="deck-board" viewBox="0 0 912 1200" xmlns="http://www.w3.org/2000/svg">
  <defs>
    <linearGradient id="gallery-tones" x1="0" y1="0" x2="0" y2="1">
      <stop offset="0" stop-color="#d9d2c4"/>
      <stop offset="0.55" stop-color="#9c8a6e"/>
      <stop offset="1" stop-color="#c9a877"/>
    </linearGradient>
    <linearGradient id="wall-tones" x1="0" y1="0" x2="1" y2="0">
      <stop offset="0" stop-color="#ecebe8"/>
      <stop offset="0.5" stop-color="#e1ddd6"/>
      <stop offset="1" stop-color="#efeeeb"/>
    </linearGradient>
    <linearGradient id="visitor-tones" x1="0" y1="0" x2="1" y2="0">
      <stop offset="0" stop-color="#e7e3de"/>
      <stop offset="0.5" stop-color="#b9ada2"/>
      <stop offset="1" stop-color="#8c7d72"/>
    </linearGradient>
    <linearGradient id="colour-tones" x1="0" y1="0" x2="1" y2="0">
      <stop offset="0" stop-color="#f1f0ea"/>
      <stop offset="0.5" stop-color="#d8c9a2"/>
      <stop offset="1" stop-color="#9fc3b0"/>
    </linearGradient>
    <linearGradient id="room-tones" x1="0" y1="0" x2="0" y2="1">
      <stop offset="0" stop-color="#cdbfae"/>
      <stop offset="0.7" stop-color="#a39383"/>
      <stop offset="1" stop-color="#d7d2cc"/>
    </linearGradient>

    <symbol id="slide-frame" viewBox="0 0 518 292">
      <rect width="518" height="292" class="white-fill"/>
      <polygon points="22,0 30,0 42,12 34,12" class="ink-fill"/>
      <polygon points="34,0 40,0 52,12 46,12" class="red-fill"/>
      <polygon points="42,0 518,0 518,12 54,12" class="red-fill"/>
      <polygon points="0,266 6,266 32,292 26,292" class="ink-fill"/>
      <polygon points="8,266 14,266 40,292 34,292" class="red-fill"/>
      <polygon points="26,280 486,280 474,292 38,292" class="red-fill"/>
      <polygon points="456,268 464,268 488,292 480,292" class="ink-fill"/>
    </symbol>

    <symbol id="cover-slide" viewBox="0 0 518 292">
      <rect width="518" height="292" class="white-fill"/>
      <polygon points="176,0 184,0 196,12 188,12" class="ink-fill"/>
      <polygon points="188,0 194,0 206,12 200,12" class="red-fill"/>
      <polygon points="196,0 518,0 518,12 208,12" class="red-fill"/>

      <rect x="17" y="22" width="98" height="25" fill="none" stroke="#333" stroke-width="1"/>
      <text x="66" y="41" text-anchor="middle" class="body-text red-fill" font-size="15">LOGO HERE</text>

      <rect x="0" y="70" width="300" height="18" class="red-fill"/>
      <polygon points="296,70 332,70 392,152 356,152" class="red-fill"/>
      <polygon points="340,70 354,70 414,152 400,152" class="red-fill"/>
      <polygon points="0,88 288,88 318,149 288,212 0,212" fill="url(#gallery-tones)" role="img" aria-label="Photo of a long museum gallery hung with classical paintings and visitors"/>
      <polyline points="292,84 326,150 292,216" fill="none" stroke="var(--brand-red)" stroke-width="7"/>
      <polygon points="334,152 518,152 518,213 300,213" class="charcoal-fill"/>
      <circle cx="349" cy="183" r="10" class="white-fill"/>
      <text x="364" y="188" class="body-text white-fill" font-size="14">@DramonteLucien</text>

      <text x="502" y="100" text-anchor="end" class="title-condensed red-fill" font-size="27">THE NEW ART</text>
      <text x="502" y="129" text-anchor="end" class="title-condensed ink-fill" font-size="27">ECONOMY</text>

      <text x="17" y="257" class="title-wide ink-fill" font-size="26" letter-spacing="2.6">AUCTION HOUSES DISRUPTED</text>

      <polygon points="0,262 6,262 32,292 26,292" class="ink-fill"/>
      <polygon points="8,262 14,262 40,292 34,292" class="red-fill"/>
      <polygon points="30,279 492,279 480,292 42,292" class="red-fill"/>
      <polygon points="486,270 494,270 514,292 506,292" class="ink-fill"/>
    </symbol>
  </defs>

  <rect x="0" y="0" width="912" height="612" fill="var(--stage-light)"/>
  <rect x="0" y="612" width="912" height="588" fill="var(--stage-grey)"/>

  <use href="#cover-slide" x="56" y="84" width="800" height="451" class="slide-shadow"/>

  <g class="slide-cover-small">
    <use href="#cover-slide" x="36" y="656" width="414" height="233" class="slide-shadow"/>
  </g>

  <g class="slide-quote" transform="translate(462 656) scale(0.7992)">
    <use href="#slide-frame" width="518" height="292" class="slide-shadow"/>
    <rect x="0" y="34" width="518" height="112" fill="url(#wall-tones)" role="img" aria-label="Photo of a visitor viewing framed portraits on a gallery wall"/>
    <text x="259" y="184" text-anchor="middle" class="quote-text ink-fill" font-size="19.5">CIVILIZATIONS ARE NOT REMEMBERED BY THEIR</text>
    <text x="259" y="210" text-anchor="middle" class="quote-text ink-fill" font-size="19.5">BUSINESS PEOPLE, BANKERS, OR LAWYERS. THEY</text>
    <text x="259" y="236" text-anchor="middle" class="quote-text ink-fill" font-size="19.5">ARE REMEMBERED BY THEIR ARTS.</text>
    <line x1="212" y1="253" x2="228" y2="253" stroke="#555" stroke-width="0.8"/>
    <text x="259" y="256" text-anchor="middle" class="body-text muted-fill" font-size="8">ARI LANDVIK</text>
    <line x1="290" y1="253" x2="306" y2="253" stroke="#555" stroke-width="0.8"/>
    <text x="500" y="276" text-anchor="end" class="body-text ink-fill" font-size="5">01</text>
  </g>

  <g class="slide-sections" transform="translate(36 926) scale(0.7992)">
    <use href="#slide-frame" width="518" height="292" class="slide-shadow"/>
    <rect x="73" y="37" width="254" height="99" fill="url(#visitor-tones)" role="img" aria-label="Photo of two visitors contemplating artworks"/>
    <rect x="327" y="37" width="126" height="99" class="red-fill"/>
    <text x="390" y="82" text-anchor="middle" class="quote-text white-fill" font-size="10">AUCTIONS TO INTERNET</text>
    <text x="390" y="97" text-anchor="middle" class="quote-text white-fill" font-size="12">THE ART</text>
    <rect x="73" y="153" width="254" height="99" fill="url(#colour-tones)" role="img" aria-label="Photo of a woman studying colourful paintings"/>
    <rect x="327" y="153" width="126" height="99" class="red-fill"/>
    <text x="390" y="199" text-anchor="middle" class="quote-text white-fill" font-size="10">MARKET IN A</text>
    <text x="390" y="212" text-anchor="middle" class="quote-text white-fill" font-size="10">CHANGING WORLD</text>
    <line x1="148" y1="286" x2="210" y2="286" stroke="#fff" stroke-width="0.6"/>
    <line x1="310" y1="286" x2="372" y2="286" stroke="#fff" stroke-width="0.6"/>
    <text x="260" y="288" text-anchor="middle" class="body-text white-fill" font-size="5" letter-spacing="1">www.loremipsum.com</text>
    <text x="500" y="276" text-anchor="end" class="body-text ink-fill" font-size="5">02</text>
  </g>

  <g class="slide-agenda" transform="translate(462 926) scale(0.7992)">
    <use href="#slide-frame" width="518" height="292" class="slide-shadow"/>
    <text x="16" y="56" class="quote-text ink-fill" font-size="15.5">AUCTIONS TO INTERNET : THE ART MARKET IN A CHANGING WORLD</text>
    <g class="agenda-list body-text" font-size="7" font-weight="700">
      <circle cx="33" cy="101" r="6" class="red-fill"/><text x="33" y="103.5" text-anchor="middle" class="white-fill">1</text>
      <text x="48" y="103.5" class="red-fill">INTRODUCTION</text>
      <circle cx="33" cy="124" r="6" class="red-fill"/><text x="33" y="126.5" text-anchor="middle" class="white-fill">2</text>
      <text x="48" y="126.5" class="red-fill">CONTEXT - A TABLE OF TWO AUCTION HOUSES</text>
      <circle cx="33" cy="148" r="6" class="red-fill"/><text x="33" y="150.5" text-anchor="middle" class="white-fill">3</text>
      <text x="48" y="150.5" class="red-fill">INTERNET &amp; GLOBALISATION :</text>
      <text x="48" y="160" class="red-fill">REVOLUTION IN THE DYNAMIC OF THE ART MARKET</text>
      <circle cx="33" cy="182" r="6" class="red-fill"/><text x="33" y="184.5" text-anchor="middle" class="white-fill">4</text>
      <text x="48" y="184.5" class="red-fill">THE AUCTION HOUSES DISRUPTED</text>
      <circle cx="33" cy="206" r="6" class="red-fill"/><text x="33" y="208.5" text-anchor="middle" class="white-fill">5</text>
      <text x="48" y="208.5" class="red-fill">BENEFITS FOR THE PRIVATE COLLECTOR?</text>
      <circle cx="33" cy="229" r="6" class="red-fill"/><text x="33" y="231.5" text-anchor="middle" class="white-fill">6</text>
      <text x="48" y="231.5" class="red-fill">CONCLUSION</text>
    </g>
    <rect x="273" y="88" width="245" height="155" fill="url(#room-tones)" role="img" aria-label="Photo of a man viewing a row of framed artworks in a gallery"/>
    <text x="500" y="276" text-anchor="end" class="body-text ink-fill" font-size="5">03</text>
  </g>
</svg>
</body>
</html>
```